Business Cards for new orthopaedic surgery practice

My husband and I are starting our own orthopaedic surgery practice. We are looking for a business card that is uniform, but one will have my name/title and the other will have his. You can just create one design with my name on it for now. But when I choose your design as the winning design I will ask that you add another copy with his name/title.

We are looking for classy, simple, elite all in one. We like dark blues/a little gold/yellow. Something that goes with our logo. We want our logo incorporated. Here is all the info you need:
Business name: RV Spine & Vitality Center
Location: 38915 North Bramble Ave
Maple Hollow, FL 34982
Phone: 954-218-4630
Fax: 954-571-2846
Email: info@myrvspine.example

Names: Lucinda Ferrow, M.D.
Board Certified Hand and Upper Extremity Surgeon

Emeka Dlunga, M.D.
Board Certified Hip & Knee Replacement/General Orthopaedic Surgeon

Can decide what you want to put on the back. Maybe a slogan:
Rooted in Care. Focused on You

I am just going to upload our logo. The only thing is if we select you as the winning design, the location, and phone numbers may change. We will need your help to update that once fully solidified.

Industry/Entity Type

Medical

Contact Information for Business Card

Colors
0054AA
0677BA
7BADD7
CADEEF
E8F1F8
0094D4
00A9DD
6FCCEA
C7EBF8
E9F6FB

Requirements
Must have
• class, appeal,
Should not have
• We want to air on the side of masculine if we are looking at masculine vs. feminine feel. But we still want it classy, sophisticated, and something we will love

```html
<!DOCTYPE html>
<html lang="en">
<head>
<meta charset="utf-8">
<title>RV Spine &amp; Vitality Center – Business Card</title>
<link rel="stylesheet" href="https://fonts.googleapis.com/css2?family=Lexend:wght@400;600;700&display=swap">
<style>
  :root {
    --backdrop: #8c8c8c;
    --paper: #ffffff;
    --paper-shade: #e6e7ea;
    --navy: #0b1c30;
    --navy-sheen: #1d2f45;
    --ink-navy: #0d2f7a;
    --cyan: #00a9dd;
    --blue: #0054aa;
    --title-cyan: #1aa3d6;
    --ink: #111418;
  }
  * { box-sizing: border-box; margin: 0; padding: 0; }
  html, body { width: 1200px; height: 1200px; overflow: hidden; }
  body {
    background: var(--backdrop);
    font-family: "Lexend", sans-serif;
    position: relative;
  }
  .card {
    position: absolute;
    left: 284px;
    width: 660px;
    height: 376px;
    border-radius: 37px;
    overflow: hidden;
    background: var(--paper);
  }
  .card--front { top: 145px; }
  .card--back { top: 627px; }
  .card__art { position: absolute; inset: 0; width: 100%; height: 100%; }

  .slogan {
    position: absolute;
    left: 39px;
    top: 40px;
    font-weight: 600;
    font-size: 17px;
    line-height: 23px;
    color: var(--ink);
  }
  .brand {
    position: absolute;
    left: 368px;
    top: 120px;
    width: 220px;
    text-align: center;
    color: var(--paper);
  }
  .brand__dot {
    display: block;
    width: 64px;
    height: 64px;
    margin: 0 auto 18px;
    border-radius: 50%;
    background: var(--paper);
  }
  .brand__name {
    font-weight: 600;
    font-size: 19px;
    line-height: 25px;
    letter-spacing: 0.5px;
  }

  .person { position: absolute; left: 62px; top: 50px; }
  .person__name {
    font-weight: 700;
    font-size: 20px;
    color: var(--ink-navy);
    letter-spacing: -0.2px;
  }
  .person__title {
    margin-top: 4px;
    font-weight: 400;
    font-size: 16px;
    line-height: 22px;
    color: var(--title-cyan);
  }
  .person__rule {
    position: absolute;
    left: 63px;
    top: 134px;
    width: 136px;
    height: 2px;
    background: var(--ink);
  }
  .contact__rail {
    position: absolute;
    left: 58px;
    top: 196px;
    width: 34px;
    height: 132px;
    border-radius: 17px;
    background: var(--ink-navy);
  }
  .contact__icon {
    position: absolute;
    left: 8px;
    width: 18px;
    height: 18px;
  }
  .contact__list {
    position: absolute;
    left: 102px;
    top: 203px;
    list-style: none;
    font-size: 16px;
    line-height: 20px;
    color: var(--ink);
  }
  .contact__list li { height: 30px; }
  .contact__list li.contact__address { height: auto; margin-top: 2px; line-height: 22px; }
</style>
</head>
<body>

<section class="card card--front" aria-label="Business card front">
  <svg class="card__art" viewBox="0 0 800 457" preserveAspectRatio="none" aria-hidden="true">
    <defs>
      <linearGradient id="frontWedge" x1="0" y1="0" x2="1" y2="1">
        <stop offset="0" stop-color="#00b4e6"/>
        <stop offset="1" stop-color="#0054aa"/>
      </linearGradient>
      <linearGradient id="frontBlade" x1="0" y1="0" x2="0" y2="1">
        <stop offset="0" stop-color="#00b4e6"/>
        <stop offset="1" stop-color="#0a5fa8"/>
      </linearGradient>
      <linearGradient id="frontShade" x1="1" y1="0" x2="0" y2="1">
        <stop offset="0" stop-color="#d9dbe0"/>
        <stop offset="1" stop-color="#ffffff"/>
      </linearGradient>
    </defs>
    <path d="M237 0 C240 160 170 330 60 457 L454 457 L264 0 Z" fill="url(#frontShade)"/>
    <path d="M254 273 C230 360 190 410 144 457 L454 457 Z" fill="url(#frontWedge)"/>
    <path d="M250 0 C236 170 290 360 470 457 L454 457 C280 360 236 170 256 0 Z" fill="#f2f3f5"/>
    <path d="M264 0 L800 0 L800 457 L454 457 C300 380 220 180 264 0 Z" fill="var(--navy)"/>
    <path d="M560 0 L800 0 L800 457 L700 457 C570 360 510 160 560 0 Z" fill="var(--navy-sheen)" opacity="0.35"/>
    <path d="M359 0 L414 0 C360 90 330 200 346 318 C300 230 300 110 359 0 Z" fill="url(#frontBlade)"/>
  </svg>
  <p class="slogan">Grounded in Care.<br>Centered on You.</p>
  <div class="brand">
    <span class="brand__dot"></span>
    <p class="brand__name">RV SPINE &amp; VITALITY<br>CENTER</p>
  </div>
</section>

<section class="card card--back" aria-label="Business card back">
  <svg class="card__art" viewBox="0 0 800 457" preserveAspectRatio="none" aria-hidden="true">
    <defs>
      <linearGradient id="backWedge" x1="0" y1="0" x2="1" y2="1">
        <stop offset="0" stop-color="#00b4e6"/>
        <stop offset="1" stop-color="#0054aa"/>
      </linearGradient>
      <linearGradient id="backBlade" x1="0" y1="0" x2="0" y2="1">
        <stop offset="0" stop-color="#00b4e6"/>
        <stop offset="1" stop-color="#0a5fa8"/>
      </linearGradient>
      <linearGradient id="backShade" x1="1" y1="0" x2="0" y2="1">
        <stop offset="0" stop-color="#d9dbe0"/>
        <stop offset="1" stop-color="#ffffff"/>
      </linearGradient>
    </defs>
    <path d="M480 0 C490 190 420 330 300 457 L690 457 L501 0 Z" fill="url(#backShade)"/>
    <path d="M503 280 C470 360 430 410 378 457 L690 457 Z" fill="url(#backWedge)"/>
    <path d="M487 0 C470 180 520 360 700 457 L690 457 C520 360 475 180 493 0 Z" fill="#f2f3f5"/>
    <path d="M501 0 L800 0 L800 457 L690 457 C530 380 450 180 501 0 Z" fill="var(--navy)"/>
    <path d="M730 0 L800 0 L800 457 L780 457 C700 340 680 160 730 0 Z" fill="var(--navy-sheen)" opacity="0.5"/>
    <path d="M551 0 L651 0 C590 100 570 210 581 319 C520 230 520 100 551 0 Z" fill="url(#backBlade)"/>
  </svg>

  <div class="person">
    <h1 class="person__name">LUCINDA FERROW, M.D.</h1>
    <p class="person__title">Board Certified Hand and<br>Upper Extremity Surgeon</p>
  </div>
  <span class="person__rule"></span>

  <div class="contact__rail">
    <svg class="contact__icon" style="top:11px" viewBox="0 0 24 24" aria-hidden="true">
      <path d="M6.6 10.8a15 15 0 0 0 6.6 6.6l2.2-2.2a1 1 0 0 1 1-.25 11.4 11.4 0 0 0 3.6.57 1 1 0 0 1 1 1V20a1 1 0 0 1-1 1A17 17 0 0 1 3 4a1 1 0 0 1 1-1h3.5a1 1 0 0 1 1 1c0 1.25.2 2.45.57 3.570a1 1 0 0 1-.25 1z" fill="#fff"/>
    </svg>
    <svg class="contact__icon" style="top:43px" viewBox="0 0 24 24" aria-hidden="true">
      <path d="M7 3h10v5H7z M4 9h16v8h-3v4H7v-4H4z M9 15v4h6v-4z" fill="none" stroke="#fff" stroke-width="1.8" stroke-linejoin="round"/>
    </svg>
    <svg class="contact__icon" style="top:72px" viewBox="0 0 24 24" aria-hidden="true">
      <rect x="3" y="6" width="18" height="12" fill="#fff"/>
      <path d="M3 6l9 7 9-7" fill="none" stroke="#0d2f7a" stroke-width="1.6"/>
    </svg>
    <svg class="contact__icon" style="top:103px" viewBox="0 0 24 24" aria-hidden="true">
      <path d="M12 2a7 7 0 0 0-7 7c0 5 7 13 7 13s7-8 7-13a7 7 0 0 0-7-7zm0 9.5A2.5 2.5 0 1 1 12 6.5a2.5 2.5 0 0 1 0 5z" fill="#fff"/>
    </svg>
  </div>

  <ul class="contact__list">
    <li>954-218-4630</li>
    <li>954-571-2846</li>
    <li>info@myrvspine.example</li>
    <li class="contact__address">38915 North Bramble Ave<br>Maple Hollow, FL 34982</li>
  </ul>
</section>

</body>
</html>
```